Independent Artist - Album Cover Design

I need a full album cover design for my debut album Velvet Tide Rising. The album is a love-inspired, passionate, soulful, relationship laden album. An album that can relate to anyone in love (or lust/obsession), going through ups and downs of relationships,and overcoming any hardships and enjoying the joys of true love, sex, and companionship. My first thoughts are a black and white design with the color red poppin off in there maybe in some of the lettering but I am open to some creative ideas. Looking for something clean and sexy that represents what the album is about. I was thinking maybe having a photo of myself on there but don't really have any that would work This Hour but I can take some and send a link if you have some good ideas.
Updates

My Artist name if I didnt mention before is Dravelle. I would like that on the album cover as well. Also I need a full album cover Front and Back. Below is the track list if you could incorporate that as well. And below is also a link to some photos. Thank you.

https://www.fileharbor.example/sh/qk4wumbrtz8plvd/KetPorvaxN

1 .Midnight Skin (Feat. Teddy Quarrelstone)
2.  Velour Heat (Feat. Dime Rek)
3 .Feel the Ember (Feat. Nalo)
4 . Lift Me Over
5. Slipshada
6.  Near Me (Feat. Dime Rek)
7 .She Wears Me Well Now
8 . This Hour
9 . All Night Again
10.  Down The Hall
11.  We Shall
12 . Seasons Of Passion

New Clearer Pictures Posted to fileharbor folder. Thanks.

https://www.fileharbor.example/sh/qk4wumbrtz8plvd/MMRt7h31FvZwQsKyNoragxunt

```html
<!DOCTYPE html>
<html lang="en">
<head>
<meta charset="utf-8">
<title>Velvet Tide Rising — Dravelle</title>
<link rel="stylesheet" href="https://fonts.googleapis.com/css2?family=Special+Elite&family=Noto+Sans+Mono:wght@300;400&display=swap">
<style>
  :root {
    --bg-deep: #161616;
    --bg-mid: #2e2e2e;
    --bg-light: #3d3d3d;
    --title-grey: #b9b9b9;
    --title-shadow: #0c0c0c;
    --track-grey: #8c8c8c;
    --artist-white: #f4f4f4;
    --photo-dark: #1c1c1c;
    --photo-light: #8a8a8a;
  }
  html, body {
    margin: 0;
    padding: 0;
    width: 1200px;
    height: 1200px;
    overflow: hidden;
    background: var(--bg-deep);
  }
  .cover {
    position: relative;
    width: 1200px;
    height: 1200px;
    overflow: hidden;
    background: radial-gradient(ellipse at 55% 45%, var(--bg-light) 0%, var(--bg-mid) 45%, var(--bg-deep) 100%);
  }
  .backdrop-pattern {
    position: absolute;
    inset: 0;
    background: radial-gradient(circle at 70% 40%, rgba(255,255,255,0.06) 0%, rgba(255,255,255,0) 55%),
                radial-gradient(circle at 20% 20%, rgba(0,0,0,0.25) 0%, rgba(0,0,0,0) 50%);
  }
  .album-title {
    position: absolute;
    top: 40px;
    left: 0;
    width: 1200px;
    margin: 0;
    text-align: center;
    font-family: "Special Elite", "Courier New", monospace;
    font-weight: 400;
    font-size: 88px;
    letter-spacing: 4px;
    color: var(--title-grey);
    text-shadow: 3px 4px 0 var(--title-shadow), 0 0 10px rgba(0,0,0,0.6);
  }
  .artist-photo {
    position: absolute;
    left: 0;
    top: 276px;
    width: 396px;
    height: 924px;
    border-top-right-radius: 180px;
    background: linear-gradient(160deg, var(--photo-dark) 0%, var(--photo-light) 45%, var(--photo-dark) 100%);
  }
  .track-list {
    position: absolute;
    left: 458px;
    top: 366px;
    margin: 0;
    padding: 0;
    list-style: none;
    font-family: "Noto Sans Mono", "Courier New", monospace;
    font-weight: 400;
    font-size: 25px;
    line-height: 49px;
    letter-spacing: 1px;
    color: var(--track-grey);
    white-space: nowrap;
  }
  .artist-name {
    position: absolute;
    left: 280px;
    bottom: 4px;
    margin: 0;
    font-family: "Noto Sans Mono", "Courier New", monospace;
    font-weight: 300;
    font-size: 128px;
    line-height: 1;
    letter-spacing: 30px;
    color: var(--artist-white);
  }
</style>
</head>
<body>
  <main class="cover">
    <div class="backdrop-pattern" role="img" aria-label="Faint dark grey ornamental pattern filling the background"></div>

    <h1 class="album-title">Velvet Tide Rising</h1>

    <div class="artist-photo" role="img" aria-label="Black and white photo of the tattooed artist in a fedora, tipping the hat brim"></div>

    <ol class="track-list">
      <li>1. Midnight Skin (Feat. Teddy Quarrelstone)</li>
      <li>2. Velour Heat (Feat. Dime Rek)</li>
      <li>3. Feel the Ember (Feat. Nalo)</li>
      <li>4. Lift Me Over</li>
      <li>5. Slipshada</li>
      <li>6. Near Me (Feat. Dime Rek)</li>
      <li>7. She Wears Me Well Now</li>
      <li>8. This Hour</li>
      <li>9. All Night Again</li>
      <li>10. Down The Hall</li>
      <li>11. We Shall</li>
      <li>12. Seasons Of Passion</li>
    </ol>

    <p class="artist-name">DRAVELLE</p>
  </main>
</body>
</html>
```